Health and Wellness company needs flyer to promote free seminar

Corelift studio is a health and wellness company that offers an exercise program designed by physical therapists to help relieve pain and improve mobility. Our business is a new concept that is not well understood by the public. In order to promote our business we offer a free seminar where we present information regarding the underlying cause of pain and tightness. During the seminar we also perform a posture screen and movement testing for all participants.

Target Market(s)

Mostly healthy and active women ages 25-65

Industry/Entity Type

Health And Wellness

Font styles to use
Sans Serif

Colors

Designer to choose colors to be used in the design.

Requirements
Must have
• Title: Eliminate Pain and Tightness For Good
• Paragraph: Corelift Studio offers a free 60 minute seminar: "The Busy Walker's Handbook to Stretching and Standing Taller."
• What to Expect:
• • Identify the underlying cause of your pain and mobility issues
• • Expose what gets in the way of you moving and feeling better
• • Learn why traditional exercises don’t help and can actually make the problem worse
• • Reveal what your posture is saying and how that impacts you
• • Experience your muscle imbalances through movement tests
• • Discover the training method that realigns your posture, increases your mobility and reduces your pain
• Call to action: RSVP online at coreliftstudio.com
Nice to have
• Use a relevant image showing a female dealing with tightness in the low back, legs, etc.
• Emphasize that the seminar is FREE.
• Make the call to action prominent.

```html
<!DOCTYPE html>
<html lang="en">
<head>
<meta charset="utf-8">
<title>Corelift Studio – Free Seminar Flyer</title>
<link rel="stylesheet" href="https://fonts.googleapis.com/css2?family=Oswald:wght@400;500;600&family=Questrial&family=Roboto+Condensed:ital,wght@0,700;1,700&display=swap">
<style>
  :root{
    --purple:#5155a6;
    --orange:#f39322;
    --ink:#3a3a3a;
    --muted:#555555;
    --paper:#ffffff;
    --stage:#e9e9ec;
    --photo-a:#dfe9f2;
    --photo-b:#f6f9fc;
    --rule:#bbbbbb;
    --frame:#9a9a9a;
  }
  *{box-sizing:border-box;margin:0;padding:0}
  html,body{width:850px;height:1200px;overflow:hidden;background:var(--stage)}
  .flyer{position:absolute;left:45px;top:67px;width:760px;height:1066px;background:var(--paper);overflow:hidden;
    box-shadow:0 4px 18px rgba(0,0,0,.12);font-family:'Questrial',sans-serif;color:var(--ink)}
  .abs{position:absolute}
  .photo{position:absolute;left:440px;top:0;width:320px;height:360px;
    background:linear-gradient(160deg,var(--photo-b) 0%,var(--photo-a) 60%,#c9dbe8 100%)}
  .swooshes{position:absolute;left:0;top:0}

  .brand{left:54px;top:31px;display:flex;align-items:center;gap:14px}
  .brand-mark{width:56px;height:56px;background:var(--orange)}
  .brand-name{font-family:'Questrial',sans-serif;font-size:34px;color:var(--purple);letter-spacing:.5px}

  .headline{left:58px;top:118px;width:380px;font-family:'Oswald',sans-serif;font-weight:500;color:var(--purple);line-height:1;text-align:right}
  .headline .row{display:block;font-size:60px}
  .headline .row-first{text-align:left}
  .headline .small{font-size:36px}
  .headline .big{font-size:74px}

  .offer{left:466px;top:470px;width:280px;font-family:'Roboto Condensed',sans-serif;font-weight:700}
  .offer .lead{font-size:25px;color:var(--ink);line-height:1.1}
  .offer .free{font-size:33px;color:var(--purple);line-height:1.1;margin-top:6px}
  .offer .title{font-style:italic;font-size:27px;color:var(--orange);line-height:1.1;margin-top:10px}

  .expect-tag{left:0;top:516px;width:345px;height:48px;background:var(--orange);color:#fff;
    clip-path:polygon(0 0,100% 0,92% 100%,0 100%);font-family:'Roboto Condensed',sans-serif;font-weight:700;font-size:32px;padding:5px 0 0 30px}
  .expect-list{left:25px;top:592px;width:410px;list-style:none}
  .expect-list li{position:relative;padding-left:26px;font-size:16px;line-height:22px;margin-bottom:12px;white-space:nowrap}
  .expect-list li::before{content:"";position:absolute;left:2px;top:5px;border-left:10px solid var(--orange);border-top:6px solid transparent;border-bottom:6px solid transparent}

  .contact-band{left:440px;top:684px;width:320px;height:36px;background:var(--purple);color:#fff;
    clip-path:polygon(4% 0,100% 0,100% 100%,0 100%);font-family:'Roboto Condensed',sans-serif;font-size:29px;padding:0 0 0 48px;line-height:36px;letter-spacing:1px}

  .studio-name{left:490px;font-size:18px;line-height:22px}
  .studio-name em{font-style:normal;color:var(--orange)}
  .studio-line{left:490px;display:flex;gap:10px;align-items:flex-start;font-size:16px;line-height:21px}
  .studio-line svg{flex:none;margin-top:2px}
  .rule{left:490px;top:848px;width:248px;height:1px;background:var(--rule)}

  .cta-label{left:278px;top:944px;width:205px;height:46px;background:var(--purple);color:#fff;border-radius:8px 8px 0 0;
    text-align:center;font-family:'Oswald',sans-serif;font-size:29px;line-height:46px;z-index:2}
  .cta-box{left:54px;top:968px;width:662px;height:82px;border:2px solid var(--frame);background:#fff;z-index:1;
    display:flex;align-items:flex-end;justify-content:center;padding-bottom:9px;
    font-family:'Oswald',sans-serif;font-weight:500;font-size:37px;color:var(--orange);letter-spacing:.5px}
  .footer-bar{left:0;bottom:0;width:760px;height:12px;background:var(--orange);border-top:3px solid var(--purple)}
</style>
</head>
<body>
<main class="flyer">
  <div class="photo" role="img" aria-label="Photo of a woman in a light blue top holding her lower back in discomfort, in a bright room"></div>

  <svg class="swooshes" width="760" height="420" viewBox="0 0 760 420" aria-hidden="true">
    <path d="M440 350 C560 320 670 280 760 240 L760 300 C650 330 520 360 380 385 C410 372 425 362 440 350 Z" fill="#ffffff"/>
    <path d="M230 400 C420 390 610 330 760 270 L760 305 C610 360 420 405 230 400 Z" fill="var(--purple)"/>
    <path d="M0 250 C120 300 220 350 330 375 C230 380 110 360 0 320 Z" fill="var(--orange)"/>
    <path d="M0 330 C100 365 200 390 300 395 C190 405 90 390 0 360 Z" fill="var(--orange)" opacity=".85"/>
  </svg>

  <div class="abs brand">
    <div class="brand-mark"></div>
    <div class="brand-name">Corelift studio</div>
  </div>

  <h1 class="abs headline">
    <span class="row row-first">ELIMINATE PAIN</span>
    <span class="row"><span class="small">AND</span>TIGHTNESS</span>
    <span class="row"><span class="small">FOR </span><span class="big">GOOD</span></span>
  </h1>

  <div class="abs offer">
    <p class="lead">CORELIFT STUDIO OFFERS</p>
    <p class="free">A FREE 60 MINUTE SEMINAR:</p>
    <p class="title">“The Busy Walker’s Handbook to Stretching and Standing Taller.”</p>
  </div>

  <h2 class="abs expect-tag">What to Expect:</h2>
  <ul class="abs expect-list">
    <li>Identify The Underlying Cause Of Your<br>Pain And Mobility Issues</li>
    <li>Expose What Gets In The Way Of You<br>Moving And Feeling Better</li>
    <li>Learn Why Traditional Exercises Don’t Help<br>And Can Actually Make The Problem Worse</li>
    <li>Reveal What Your Posture Is Saying<br>And How That Impacts You</li>
    <li>Experience Your Muscle Imbalances<br>Through Movement Tests</li>
    <li>Discover The Training Method<br>That Realigns Your Posture,<br>Increases Your Mobility And Reduces Your Pain</li>
  </ul>

  <h2 class="abs contact-band">Contact us:</h2>

  <p class="abs studio-name" style="top:734px">Studio <em>Houston</em></p>
  <p class="abs studio-line" style="top:762px"><svg width="18" height="18" viewBox="0 0 18 18"><circle cx="9" cy="9" r="8" fill="none" stroke="#555" stroke-width="1.4"/><path d="M9 4a3 3 0 0 0-3 3c0 2.3 3 6 3 6s3-3.7 3-6a3 3 0 0 0-3-3z" fill="#555"/></svg><span>4870 Larkspur Avenue,<br>Houston, TX 77008</span></p>
  <p class="abs studio-line" style="top:814px"><svg width="18" height="18" viewBox="0 0 18 18"><circle cx="9" cy="9" r="8" fill="none" stroke="#555" stroke-width="1.4"/><path d="M6 5l2 0 1 2-1 1c.5 1 1.5 2 2.5 2.5l1-1 2 1v2c-4 .5-8-3.5-7.5-7.5z" fill="#555"/></svg><span>(281) 555-0142</span></p>

  <div class="abs rule"></div>

  <p class="abs studio-name" style="top:858px">Studio <em>Portland</em></p>
  <p class="abs studio-line" style="top:885px"><svg width="18" height="18" viewBox="0 0 18 18"><circle cx="9" cy="9" r="8" fill="none" stroke="#555" stroke-width="1.4"/><path d="M9 4a3 3 0 0 0-3 3c0 2.3 3 6 3 6s3-3.7 3-6a3 3 0 0 0-3-3z" fill="#555"/></svg><span>2390 SE Alder Lane<br>#12 Milwaukie, OR 97222</span></p>
  <p class="abs studio-line" style="top:935px"><svg width="18" height="18" viewBox="0 0 18 18"><circle cx="9" cy="9" r="8" fill="none" stroke="#555" stroke-width="1.4"/><path d="M6 5l2 0 1 2-1 1c.5 1 1.5 2 2.5 2.5l1-1 2 1v2c-4 .5-8-3.5-7.5-7.5z" fill="#555"/></svg><span>(503) 555-0178</span></p>

  <div class="abs cta-label">CALL TO ACTION:</div>
  <div class="abs cta-box">RSVP ONLINE AT CORELIFTSTUDIO.COM</div>

  <div class="abs footer-bar"></div>
</main>
</body>
</html>
```